Business Card for premium dental clinic

We are a premium dental clinic based in Brasov, Romania with more than 15 year on the market, providing quality dental treatment made by a team of more specialized dentists, working with modern equipment as a solution to beautiful and healthy teeth.

Our current logo for the clinic use 2 square with colors black and gold - dr Corbescu - studio, using family fonts Bodoni, Myriad Pro and Segoe Print.
Depending on the printing we used some gold CMYK background or gold foil picture background or a gold gradient.
We want a business card:
- eye catching business card
- distinguished business card
- premium design
- to keep the color scheme of black and gold
- to attract the customers to spent time reading the information
- modern concept

```html
<!DOCTYPE html>
<html lang="en">
<head>
<meta charset="utf-8">
<title>dr Corbescu – Business Card</title>
<link href="https://fonts.googleapis.com/css2?family=PT+Sans:wght@400;700&display=swap" rel="stylesheet">
<style>
  :root {
    --backdrop: #5e4c38;
    --card-white: #ffffff;
    --card-black: #000000;
    --gold: #f2b820;
    --gold-deep: #d99a12;
    --ink: #111111;
    --text-light: #ffffff;
  }
  * { margin: 0; padding: 0; box-sizing: border-box; }
  html, body {
    width: 1189px; height: 1200px; overflow: hidden;
    background: var(--backdrop);
    font-family: "PT Sans", "Myriad Pro", sans-serif;
  }
  .canvas { position: relative; width: 1189px; height: 1200px; }

  .card {
    position: absolute; left: 169px; width: 851px; height: 486px;
    border-radius: 34px; overflow: hidden;
    background: var(--card-white);
    box-shadow: 0 4px 14px rgba(0,0,0,0.35);
  }
  .card--front { top: 112px; }
  .card--back  { top: 641px; }

  .brand {
    position: absolute; display: flex; align-items: center; gap: 14px;
    transform: translate(-50%, -50%);
    white-space: nowrap;
  }
  .brand__mark { width: 30px; height: 30px; background: var(--gold); flex: none; }
  .brand__name { font-size: 42px; font-weight: 400; color: var(--ink); letter-spacing: 0.5px; }
  .card--front .brand { left: 426px; top: 242px; }
  .card--back .brand { left: 213px; top: 243px; }
  .card--back .brand__name { font-size: 38px; }

  .contact-panel {
    position: absolute; left: 426px; top: 0; right: 0; bottom: 0;
    background: var(--card-black); color: var(--text-light);
  }
  .person { position: absolute; left: 60px; top: 126px; }
  .person__name { font-size: 28px; font-weight: 700; line-height: 1.05; }
  .person__role { font-size: 20px; color: var(--gold); line-height: 1.1; }

  .address { position: absolute; left: 60px; top: 200px; font-size: 19px; line-height: 27px; }

  .contacts { position: absolute; left: 59px; top: 274px; list-style: none; font-size: 19px; }
  .contacts li { display: flex; align-items: center; gap: 12px; height: 31.5px; }
  .contacts svg { width: 22px; height: 22px; flex: none; }
</style>
</head>
<body>
<main class="canvas">
  <section class="card card--front" aria-label="Card front">
    <div class="brand">
      <span class="brand__mark"></span>
      <span class="brand__name">dr Corbescu</span>
    </div>
  </section>

  <section class="card card--back" aria-label="Card back">
    <div class="brand">
      <span class="brand__mark"></span>
      <span class="brand__name">dr Corbescu</span>
    </div>

    <div class="contact-panel">
      <div class="person">
        <p class="person__name">Andrei Popa</p>
        <p class="person__role">Manager</p>
      </div>
      <p class="address">PO BOX 48, Str. Lunga 12<br>Centru, Brasov</p>
      <ul class="contacts">
        <li>
          <svg viewBox="0 0 22 22" aria-hidden="true">
            <circle cx="11" cy="11" r="11" fill="var(--gold)"/>
            <path d="M8 5.5c.6-.4 1.3-.2 1.6.4l1 2c.3.6.1 1.2-.4 1.5l-.7.5c.5 1.4 1.4 2.5 2.7 3.2l.6-.6c.5-.4 1.1-.4 1.5.1l1.3 1.5c.4.5.3 1.2-.2 1.6l-.9.7c-3.6-.5-6.9-4.4-6.9-8.3z" fill="var(--card-black)"/>
          </svg>
          <span>(268) 555 0142</span>
        </li>
        <li>
          <svg viewBox="0 0 22 22" aria-hidden="true">
            <circle cx="11" cy="11" r="11" fill="var(--gold)"/>
            <rect x="5.5" y="7.5" width="11" height="7.5" fill="none" stroke="var(--card-black)" stroke-width="1.3"/>
            <path d="M5.5 7.5l5.5 4.3 5.5-4.3M5.5 15l4-3.5M16.5 15l-4-3.5" fill="none" stroke="var(--card-black)" stroke-width="1.1"/>
          </svg>
          <span>hello@corbescustudio.ro</span>
        </li>
        <li>
          <svg viewBox="0 0 22 22" aria-hidden="true">
            <circle cx="11" cy="11" r="11" fill="var(--gold)"/>
            <g fill="none" stroke="var(--card-black)" stroke-width="1.1">
              <circle cx="11" cy="11" r="6"/>
              <ellipse cx="11" cy="11" rx="2.6" ry="6"/>
              <path d="M5 11h12M6 8h10M6 14h10"/>
            </g>
          </svg>
          <span>www.corbescustudio.ro</span>
        </li>
      </ul>
    </div>
  </section>
</main>
</body>
</html>
```